Web Design for an Online Dating Web Site

We need an uncoded web design for a new online dating web site called zMatchy.net. Simplicity and boldness are the key factors in the successful design.
Please look at the requirements document attached for details.
Updates
Dear all,
Please AVOID USING A PICTURE OF A HAPPY COUPLE ON THE HOME PAGE of the site. We highly want to move away from this space as it makes our web site just like another dating web site.
We like something simple with web 2.0 look and feel. The examples in the Requirements Document are exactly the design we are after.
Regards
Tarn
Industry/Entity Type
Dating
Look and feel
Each slider illustrates characteristics of the customer's brand and the style your logo design should communicate.

```html
<!DOCTYPE html>
<html lang="en">
<head>
<meta charset="utf-8">
<title>zMatchy.net – Online Dating</title>
<link rel="stylesheet" href="https://fonts.googleapis.com/css2?family=Oswald:wght@300;400&family=Open+Sans:wght@400;600&display=swap">
<style>
:root{
  --pink:#e4147e;
  --pink-deep:#a4004f;
  --pink-band:#d0106e;
  --grey-text:#6a6a6a;
  --grey-light:#e9e9e9;
  --grey-mid:#c9c9c9;
  --white:#ffffff;
  --footer-dark:#4a4a4a;
  --footer-mid:#6b6b6b;
  --field:#5a5a5a;
}
*{box-sizing:border-box;margin:0;padding:0}
html,body{width:947px;height:1200px;overflow:hidden}
body{position:relative;background:#dcdcdc;font-family:"Open Sans",sans-serif;color:var(--grey-text)}
.abs{position:absolute}
.head-font{font-family:"Oswald",sans-serif;font-weight:400;text-transform:uppercase}

/* header */
.site-header{left:0;top:0;width:947px;height:200px;background:linear-gradient(#f6f6f6,#dedede)}
.nav-band{left:0;top:132px;width:560px;height:48px;background:linear-gradient(90deg,#ececec,#f7f7f7 70%,rgba(240,240,240,0))}
.brand{left:94px;top:40px;display:flex;align-items:center;gap:10px}
.brand-dot{width:26px;height:26px;border-radius:50%;background:var(--pink)}
.brand-name{font-family:"Open Sans",sans-serif;font-weight:600;font-size:46px;color:var(--pink);letter-spacing:-1px}
.main-nav{left:93px;top:146px;display:flex;gap:23px;font-size:15px;color:#666}
.main-nav .active{color:var(--pink)}
.login-box{left:552px;top:24px;width:299px;height:124px;background:var(--white);border-radius:3px;box-shadow:0 2px 4px rgba(0,0,0,.2)}
.login-title{left:14px;top:14px;font-size:17px;color:#555;display:flex;align-items:center;gap:8px}
.login-title span{color:var(--pink)}
.lock{width:11px;height:10px;background:#aaa;border-radius:1px;position:relative}
.lock:before{content:"";position:absolute;left:2px;top:-6px;width:7px;height:8px;border:2px solid #aaa;border-bottom:none;border-radius:4px 4px 0 0}
.field{height:24px;background:#f1f1f1;border-bottom:1px solid #ddd;font-size:10px;font-style:italic;color:#777;padding:5px 12px}
.login-user{left:12px;top:46px;width:132px}
.login-pass{left:155px;top:46px;width:132px}
.login-btn{left:12px;top:81px;width:82px;height:26px;border-radius:4px;background:linear-gradient(#dedede,#a9a9a9);color:#555;font-size:13px;text-align:center;line-height:26px}
.login-or{left:106px;top:85px;font-style:italic;font-weight:600;font-size:14px;color:#666}
.login-alt{left:130px;top:88px;display:flex;gap:7px;font-size:9px;color:#777}
.login-alt .more{color:var(--pink);font-size:12px;margin-left:2px;margin-top:-2px}

/* slider */
.slider{left:0;top:201px;width:947px;height:316px;background:radial-gradient(ellipse at 55% 45%,#ec2a8c,var(--pink-band) 55%,var(--pink-deep))}
.slide-visual{left:95px;top:41px;width:407px;height:236px;background:radial-gradient(circle at 45% 45%,#ffd3e8,#ffffff 70%);box-shadow:0 14px 14px -8px rgba(0,0,0,.5)}
.slide-title{left:528px;top:58px;font-size:34px;color:var(--white);font-weight:400}
.slide-text{left:528px;top:104px;width:330px;font-size:16px;line-height:19.5px;color:#ffe3f0}
.read-more{left:538px;top:209px;width:205px;height:50px;border-radius:25px;background:linear-gradient(#f0f0f0,#bdbdbd);box-shadow:0 0 0 3px rgba(255,255,255,.35);font-size:28px;color:#777;text-align:center;line-height:50px}
.arrow{top:122px;width:66px;height:72px}
.arrow-prev{left:6px}
.arrow-next{left:874px}

/* middle */
.content{left:0;top:517px;width:947px;height:448px;background:linear-gradient(90deg,#d0d0d0,#eeeeee 45%,#f2f2f2 60%,#d2d2d2)}
.video{left:115px;top:38px;width:387px;height:236px;background:#e4e4e4;border:3px solid var(--white);box-shadow:0 0 12px 4px rgba(228,20,126,.8)}
.play{left:146px;top:72px;width:90px;height:90px}
.signup-btn{left:114px;top:318px;width:262px;height:72px;background:linear-gradient(#e4e4e4,#b4b4b4);border:2px solid #ededed;box-shadow:0 3px 4px rgba(0,0,0,.4);font-size:44px;color:#707070;text-align:center;line-height:68px;font-weight:300}
.curve-arrow{left:390px;top:288px;width:120px;height:110px}
.posts{left:545px;top:32px;width:306px;height:394px;background:var(--white);border:1px solid #ddd;border-radius:3px}
.posts-title{left:18px;top:10px;font-size:22px;color:#666;font-weight:300}
.posts-title span{color:var(--pink)}
.posts-head-shade{left:0;top:0;width:304px;height:52px;background:linear-gradient(#fff,#f1f1f1);border-bottom:1px solid #e6e6e6}
.post{left:0;width:304px;height:98px;border-bottom:1px solid #e8e8e8}
.post-thumb{left:20px;top:22px;width:55px;height:55px;border:2px solid #fff;box-shadow:0 1px 3px rgba(0,0,0,.4)}
.post-title{left:92px;top:14px;font-size:15px;color:var(--pink)}
.post-text{left:92px;top:41px;width:200px;font-size:9px;line-height:11px;color:#666}
.post-meta{left:92px;top:85px;font-size:7.5px;color:#777}

/* footer */
.site-footer{left:0;top:965px;width:947px;height:235px;background:linear-gradient(90deg,#4c4c4c,#6e6e6e 50%,#404040);border-top:3px solid #999}
.foot-brand{left:90px;top:86px;display:flex;align-items:center;gap:7px}
.foot-brand .brand-dot{width:16px;height:16px}
.foot-brand .brand-name{font-size:28px}
.foot-head{font-size:16px;color:#eee}
.foot-head span{color:#aaa}
.foot-rule{height:1px;background:#888}
.foot-links{left:283px;top:57px;list-style:none;font-size:11.5px;color:#eee;line-height:24px}
.foot-field{background:var(--field);border-radius:3px;font-size:11px;font-style:italic;color:#ccc;padding:5px 13px}
.send-btn{left:481px;top:186px;width:80px;height:24px;border-radius:3px;background:linear-gradient(#ddd,#aaa);color:#666;font-size:13px;text-align:center;line-height:24px}
.social{left:680px;top:60px;width:175px;display:flex;flex-wrap:wrap;gap:6px 4px}
.social-item{width:40px;height:40px;border-radius:50%;background:linear-gradient(#e8e8e8,#a8a8a8);color:#555;font-size:7.5px;font-weight:600;display:flex;align-items:center;justify-content:center}
.share{display:flex;gap:3px;font-size:8.5px}
.share-btn{background:#eef3fa;border:1px solid #b5c4dd;border-radius:2px;color:#3b5998;padding:1px 5px}
.share-count{background:#fff;border:1px solid #b5c4dd;border-radius:2px;color:#3b5998;padding:1px 4px}
</style>
</head>
<body>

<header class="site-header abs">
  <div class="nav-band abs"></div>
  <div class="brand abs"><span class="brand-dot"></span><span class="brand-name">zMatchy.net</span></div>
  <nav class="main-nav abs head-font">
    <span class="active">Why</span><span>How it works</span><span>Sign up</span><span>Our blog</span>
  </nav>
  <div class="login-box abs">
    <div class="login-title abs head-font"><i class="lock"></i>User <span>Login</span></div>
    <div class="field login-user abs">username</div>
    <div class="field login-pass abs">password</div>
    <div class="login-btn abs head-font">Login</div>
    <div class="login-or abs">or</div>
    <div class="login-alt abs"><span>Postly</span><span>Yodel</span><span>Glimr</span><span>Livio</span><span class="more">More</span></div>
  </div>
</header>

<section class="slider abs">
  <svg class="arrow arrow-prev abs" viewBox="0 0 66 72"><path d="M60 6 L30 6 Q4 6 4 36 Q4 66 30 66 L60 66 Q46 52 46 36 Q46 20 60 6Z" fill="#ececec" stroke="#fff" stroke-width="2"/><path d="M38 22 L24 36 L38 50" fill="none" stroke="#e4147e" stroke-width="8" stroke-linecap="round"/></svg>
  <div class="slide-visual abs" role="img" aria-label="Illustration of pink hearts connected by a cable to a computer mouse"></div>
  <h2 class="slide-title abs head-font">Key Difference</h2>
  <p class="slide-text abs">It is a long established fact that a reader will be distracted by the readable content of a page when looking at its layout.</p>
  <div class="read-more abs head-font">Read more</div>
  <svg class="arrow arrow-next abs" viewBox="0 0 66 72"><path d="M6 6 L36 6 Q62 6 62 36 Q62 66 36 66 L6 66 Q20 52 20 36 Q20 20 6 6Z" fill="#ececec" stroke="#fff" stroke-width="2"/><path d="M28 22 L42 36 L28 50" fill="none" stroke="#e4147e" stroke-width="8" stroke-linecap="round"/></svg>
</section>

<main class="content abs">
  <div class="video abs">
    <svg class="play abs" viewBox="0 0 90 90"><circle cx="45" cy="45" r="43" fill="#dadada" stroke="#cfcfcf" stroke-width="2"/><circle cx="45" cy="45" r="36" fill="#e6e6e6"/><path d="M33 27 L63 45 L33 63Z" fill="#e4147e"/></svg>
  </div>
  <div class="signup-btn abs head-font">Sign up</div>
  <svg class="curve-arrow abs" viewBox="0 0 120 110"><path d="M100 0 Q130 60 70 82 L74 100 L6 72 L58 40 L62 60 Q100 50 100 0Z" fill="#dcdcdc" opacity=".8"/></svg>

  <aside class="posts abs">
    <div class="posts-head-shade abs"></div>
    <h3 class="posts-title abs head-font">Recent <span>posts</span></h3>
    <article class="post abs" style="top:55px">
      <div class="post-thumb abs" style="background:linear-gradient(135deg,#c33 0%,#333 55%,#999)" role="img" aria-label="Post photo in dark tones with red"></div>
      <h4 class="post-title abs head-font">Post title goes here</h4>
      <p class="post-text abs">It is a long established fact that a reader will be distracted by the readable content of a page when looking at its layout.</p>
      <p class="post-meta abs">Posted Oct 01, 2011 | 5 Comments | Read More</p>
    </article>
    <article class="post abs" style="top:153px">
      <div class="post-thumb abs" style="background:linear-gradient(135deg,#8a7a60,#c3b08a 50%,#6a5d48)" role="img" aria-label="Post photo of a heart drawn in sand"></div>
      <h4 class="post-title abs head-font">Post title goes here</h4>
      <p class="post-text abs">It is a long established fact that a reader will be distracted by the readable content of a page when looking at its layout.</p>
      <p class="post-meta abs">Posted Oct 01, 2011 | 5 Comments | Read More</p>
    </article>
    <article class="post abs" style="top:251px;border-bottom:none">
      <div class="post-thumb abs" style="background:radial-gradient(circle,#f0f4fa,#6d8fb8 70%)" role="img" aria-label="Post photo of a heart-shaped cloud in a blue sky"></div>
      <h4 class="post-title abs head-font">Post title goes here</h4>
      <p class="post-text abs">It is a long established fact that a reader will be distracted by the readable content of a page when looking at its layout.</p>
      <p class="post-meta abs">Posted Oct 01, 2011 | 5 Comments | Read More</p>
    </article>
  </aside>
</main>

<footer class="site-footer abs">
  <div class="foot-brand abs"><span class="brand-dot"></span><span class="brand-name">zMatchy.net</span></div>

  <h4 class="foot-head abs head-font" style="left:283px;top:18px">Read <span>more</span></h4>
  <div class="foot-rule abs" style="left:283px;top:42px;width:184px"></div>
  <ul class="foot-links abs">
    <li>Why zMatchy</li><li>How it works</li><li>Sign Up</li><li>Login</li><li>About Us</li>
  </ul>

  <h4 class="foot-head abs head-font" style="left:481px;top:18px">Let's <span>talk</span></h4>
  <div class="foot-rule abs" style="left:481px;top:42px;width:184px"></div>
  <div class="foot-field abs" style="left:481px;top:60px;width:184px;height:24px">Name</div>
  <div class="foot-field abs" style="left:481px;top:91px;width:184px;height:24px">E-mail</div>
  <div class="foot-field abs" style="left:481px;top:123px;width:184px;height:56px">Comment</div>
  <div class="send-btn abs head-font">Send</div>

  <div class="social abs">
    <span class="social-item">Facely</span><span class="social-item">Chirpr</span>
    <span class="social-item">
      <svg width="22" height="22" viewBox="0 0 22 22"><circle cx="4" cy="18" r="3" fill="#555"/><path d="M2 9 A11 11 0 0 1 13 20 M2 2 A18 18 0 0 1 20 20" fill="none" stroke="#555" stroke-width="3"/></svg>
    </span>
    <span class="social-item">Snapr</span><span class="social-item">Vidora</span><span class="social-item">Tastee</span><span class="social-item">Stumblr</span><span class="social-item">Linkwise</span>
  </div>
  <div class="share abs" style="left:692px;top:165px">
    <span class="share-btn">Like</span><span class="share-count">10,000</span>
    <span class="share-btn">Chirp</span><span class="share-count">10,000</span>
  </div>
  <div class="share abs" style="left:735px;top:189px">
    <span class="share-btn">Plus</span><span class="share-count">10,000</span>
  </div>
</footer>

</body>
</html>
```